RK Bastone Construction Inc.

Design a new business card for our construction company
To be removed from current card:
Delete 25 years
Delete Tenant fit up Renovations section

```html
<!DOCTYPE html>
<html lang="en">
<head>
<meta charset="utf-8">
<title>RK Bastone Construction Inc. – Business Card</title>
<link href="https://fonts.googleapis.com/css2?family=Archivo:wght@800&family=Arimo:wght@400;700&display=swap" rel="stylesheet">
<style>
  :root {
    --teal: #1b7369;
    --teal-light: #238577;
    --purple: #4e2a72;
    --paper: #ffffff;
    --backdrop: #e9e7e3;
  }
  * { box-sizing: border-box; margin: 0; padding: 0; }
  html, body { width: 1200px; height: 900px; overflow: hidden; }
  body { background: var(--backdrop); position: relative; font-family: "Arimo", Arial, sans-serif; }

  .card {
    position: absolute;
    width: 700px; height: 400px;
    background: var(--paper);
    box-shadow: 0 6px 18px rgba(0,0,0,.18);
    overflow: hidden;
  }
  .card--front { left: 140px; top: 38px; }
  .card--back  { left: 360px; top: 462px; }

  .card__band { position: absolute; inset: 0; width: 100%; height: 100%; }

  .wordmark {
    position: absolute;
    display: flex; align-items: center; gap: 14px;
    font-family: "Archivo", sans-serif; font-weight: 800;
    color: var(--purple); text-transform: uppercase; line-height: 1.02;
  }
  .wordmark__square { width: 22px; height: 22px; background: var(--purple); flex: none; }
  .card--front .wordmark { left: 170px; top: 92px; font-size: 40px; letter-spacing: 1px; }
  .card--back .wordmark { left: 44px; top: 58px; font-size: 34px; letter-spacing: 1px; }

  .web-line {
    position: absolute; right: 34px; bottom: 22px;
    font-family: "Arimo", sans-serif; font-weight: 700; font-size: 15px;
    letter-spacing: 6px; color: var(--purple);
  }
  .web-line__prefix { color: var(--paper); }

  .holder {
    position: absolute; left: 92px; top: 172px;
    font-family: "Archivo", sans-serif; font-weight: 800; font-size: 19px;
    color: var(--teal); letter-spacing: .5px; text-transform: uppercase;
  }
  .contacts { position: absolute; left: 92px; top: 210px; list-style: none; }
  .contacts__item {
    display: flex; align-items: center; gap: 10px;
    font-size: 16px; color: var(--purple); height: 26px;
  }
  .contacts__icon { width: 16px; height: 16px; flex: none; }

  .address {
    position: absolute; left: 48px; bottom: 20px;
    display: flex; align-items: center; gap: 10px;
    color: var(--paper); font-size: 17px;
  }
</style>
</head>
<body>

  <!-- Front of card -->
  <section class="card card--front">
    <svg class="card__band" viewBox="0 0 700 400" preserveAspectRatio="none" aria-hidden="true">
      <path d="M0 400 L0 318 Q140 262 300 282 L310 282 Q330 290 340 322 L700 226 L700 260 Z" fill="var(--teal)" transform="translate(0 0)"/>
      <path d="M0 400 L0 318 Q140 262 300 282 L320 290 L700 170 L700 400 Z" fill="var(--teal)" opacity="0"/>
      <path d="M0 400 V318 Q150 262 320 290 L700 200 V400 Z" fill="var(--teal)"/>
      <path d="M0 300 Q150 246 320 272" fill="none" stroke="var(--teal)" stroke-width="4"/>
    </svg>
    <div class="wordmark">
      <span class="wordmark__square"></span>
      <span>RK Bastone<br>Construction Inc.</span>
    </div>
    <p class="web-line"><span class="web-line__prefix">www.</span>rkbastoneconstruction.ca</p>
  </section>

  <!-- Back of card -->
  <section class="card card--back">
    <svg class="card__band" viewBox="0 0 700 400" preserveAspectRatio="none" aria-hidden="true">
      <path d="M0 400 V340 L440 340 Q480 300 700 286 V400 Z" fill="var(--teal)"/>
      <path d="M450 324 Q520 282 700 266" fill="none" stroke="var(--teal)" stroke-width="4"/>
    </svg>
    <div class="wordmark">
      <span class="wordmark__square"></span>
      <span>RK Bastone<br>Construction Inc.</span>
    </div>

    <p class="holder">Marco Bastone</p>
    <ul class="contacts">
      <li class="contacts__item">
        <svg class="contacts__icon" viewBox="0 0 16 16"><rect x="4" y="1" width="8" height="14" rx="1.5" fill="none" stroke="var(--purple)" stroke-width="1.6"/><circle cx="8" cy="12.5" r=".9" fill="var(--purple)"/></svg>
        613-555-0142
      </li>
      <li class="contacts__item">
        <svg class="contacts__icon" viewBox="0 0 16 16"><path d="M2 6 Q8 1 14 6 L12 8 L10 6.5 H6 L4 8 Z" fill="var(--purple)"/><rect x="4" y="9" width="8" height="5" rx="1" fill="var(--purple)"/></svg>
        613-555-0187 ext.221
      </li>
      <li class="contacts__item">
        <svg class="contacts__icon" viewBox="0 0 16 16"><rect x="1.5" y="4" width="13" height="9" rx="1" fill="var(--purple)"/><path d="M1.5 4 L8 9 L14.5 4" fill="none" stroke="#fff" stroke-width="1.2"/></svg>
        marco@rkbastoneconstruction.ca
      </li>
      <li class="contacts__item">
        <svg class="contacts__icon" viewBox="0 0 16 16"><circle cx="8" cy="8" r="6.3" fill="none" stroke="var(--purple)" stroke-width="1.5"/><ellipse cx="8" cy="8" rx="2.6" ry="6.3" fill="none" stroke="var(--purple)" stroke-width="1.2"/><path d="M2 8 H14" stroke="var(--purple)" stroke-width="1.2"/></svg>
        www.rkbastoneconstruction.ca
      </li>
    </ul>

    <p class="address">
      <svg class="contacts__icon" viewBox="0 0 16 16"><path d="M8 15 C4 10 3 8 3 6 A5 5 0 0 1 13 6 C13 8 12 10 8 15 Z" fill="var(--purple)"/><circle cx="8" cy="6" r="1.8" fill="var(--teal)"/></svg>
      2180 Fernbank Rd. Suite 100, Ottawa, ON K2S4B7
    </p>
  </section>

</body>
</html>
```